Logistics and freight company requires website

Hi, a logistic and freight company which is based in the United States needs an industry standard website for its activities. We are into forwarding and courier goods from within United States and Canada. We deliver a wide range of goods from shipping of electronics to document, clothings, etc. The proposed website should be comtemporary and youthful. I require brilliant colors for the website. The website should be the basic things of a site. There should a category for shipping electronics, clothings, documents and others( stuffs not listed within the three I mentioned).

```html
<!DOCTYPE html>
<html lang="en">
<head>
<meta charset="utf-8">
<title>Northbeam Freight — Cargo Transport</title>
<link rel="stylesheet" href="https://fonts.googleapis.com/css2?family=Raleway:wght@400;500;600;700;800&display=swap">
<style>
:root{
  --backdrop:#a9a9a9;
  --sky-top:#0b2f9e;
  --sky-mid:#1f63e0;
  --sky-light:#4fa3ff;
  --footer:#0b4fb8;
  --blue:#1f7bff;
  --blue-dark:#0f5fd6;
  --cyan:#37c2ff;
  --ink:#2b2b2b;
  --muted:#555;
  --white:#fff;
  --card-line:#e4e4e4;
  --font:'Raleway',Arial,sans-serif;
}
*{box-sizing:border-box;margin:0;padding:0}
html,body{width:960px;height:1200px;overflow:hidden;background:var(--backdrop);font-family:var(--font)}
.page{position:absolute;left:167px;top:0;width:780px;height:1500px;transform:scale(.8);transform-origin:0 0;background:var(--white);overflow:hidden}
.fill-area{position:absolute;inset:0}

/* hero */
.hero{position:absolute;left:0;top:0;width:780px;height:360px;background:linear-gradient(160deg,var(--sky-top) 0%,var(--sky-mid) 48%,var(--sky-light) 72%,#1a56cf 100%);color:var(--white)}
.topbar{position:absolute;left:0;top:0;width:780px;height:26px;border-bottom:1px solid rgba(255,255,255,.18);font-size:8px}
.topbar-links{position:absolute;left:48px;top:9px;display:flex;gap:10px;align-items:center}
.topbar-links span::before{content:"";display:inline-block;width:7px;height:6px;background:var(--white);margin-right:4px;border-radius:1px}
.social{position:absolute;left:530px;top:10px;display:flex;gap:13px}
.social i{display:block;width:6px;height:6px;border-radius:50%;background:var(--white)}
.fare{position:absolute;left:633px;top:5px;width:91px;height:17px;background:var(--blue);font-size:7.5px;font-weight:600;line-height:17px;text-align:center}
.brand{position:absolute;left:44px;top:38px;font-size:8px;font-weight:500}
.nav{position:absolute;left:444px;top:49px;display:flex;gap:17px;font-size:8px;font-weight:700}
.nav span:first-child{color:#d4e3ff;font-weight:500}
.welcome{position:absolute;left:44px;top:138px;font-size:13px;font-weight:600}
.title{position:absolute;left:43px;top:160px;font-size:30px;font-weight:800;letter-spacing:.3px}
.rule{position:absolute;left:44px;top:204px;width:50px;height:2px;background:var(--cyan)}
.lead{position:absolute;left:44px;top:215px;width:360px;font-size:12.5px;line-height:21px}
.btn{position:absolute;top:283px;height:20px;font-size:7.5px;font-weight:700;line-height:20px;text-align:center}
.btn.primary{left:44px;width:94px;background:var(--blue)}
.btn.ghost{left:150px;width:84px;background:#56657d}
.quote{position:absolute;left:460px;top:108px;width:264px;height:230px;background:rgba(12,30,80,.78);padding:12px}
.quote h3{font-size:12px;font-weight:700}
.quote .note{font-size:6.5px;margin-top:3px}
.field{position:absolute;left:12px;font-size:7px;font-weight:600}
.select{position:absolute;left:82px;width:170px;height:16px;border:1px solid #8da2c8;background:#eef3fb;color:#888;font-size:7px;line-height:14px;padding-left:7px}
.select::after{content:"";position:absolute;right:6px;top:4px;width:4px;height:4px;border-right:1.5px solid #333;border-bottom:1.5px solid #333;transform:rotate(45deg)}
.slider{position:absolute;left:92px;top:137px;width:160px;height:8px;border:1px solid #8da2c8;border-radius:4px}
.knob{position:absolute;left:82px;top:130px;width:22px;height:22px;border-radius:50%;background:var(--blue);font-size:6px;color:var(--white);text-align:center;line-height:22px}
.toggle{position:absolute;left:82px;top:160px;width:45px;height:22px;border-radius:11px;border:1px solid #8da2c8;background:#34487a}
.toggle::before{content:"";position:absolute;left:3px;top:3px;width:15px;height:15px;border-radius:50%;background:#e3e3e3}
.total{position:absolute;left:12px;top:194px;width:240px;height:24px;background:var(--blue);font-size:7.5px;font-weight:700;line-height:24px}
.total .lbl{position:absolute;right:63px}
.total .val{position:absolute;right:0;width:48px;height:24px;background:var(--blue-dark);text-align:center}
.next{position:absolute;left:740px;top:193px}

/* categories */
.services{position:absolute;left:0;top:360px;width:780px;height:333px;background:var(--white)}
.map-dots{position:absolute;left:20px;top:10px;width:740px;height:300px;background:radial-gradient(ellipse at 30% 45%,#eef2f7 0%,rgba(255,255,255,0) 58%),radial-gradient(ellipse at 72% 28%,#f0f3f7 0%,rgba(255,255,255,0) 52%)}
.kicker{position:absolute;right:528px;top:48px;font-size:8px;font-weight:600;color:var(--ink);text-align:right}
.sec-title{position:absolute;right:528px;top:62px;font-size:17px;font-weight:800;line-height:26px;text-align:right;color:var(--ink)}
.path{position:absolute;left:40px;top:202px;width:222px;font-size:7.5px;line-height:15px;text-align:right;color:#444}
.card{position:absolute;width:219px;height:115px;background:var(--white);border:1px solid var(--card-line);box-shadow:0 1px 3px rgba(0,0,0,.08);padding:28px 16px 0 43px}
.card svg{position:absolute;left:14px;top:25px}
.card h4{font-size:8.5px;font-weight:700;color:var(--ink)}
.card p{font-size:7px;line-height:14.5px;color:#444;margin-top:8px}

/* numbers */
.numbers{position:absolute;left:0;top:692px;width:780px;height:281px;background:linear-gradient(165deg,#123a8c 0%,#1d56bf 42%,#14408f 75%,#1b4fae 100%);color:var(--white)}
.kicker2{position:absolute;right:528px;top:60px;font-size:8px;font-weight:600}
.numbers h2{position:absolute;right:528px;top:76px;font-size:17px;font-weight:800}
.numbers blockquote{position:absolute;left:80px;top:128px;width:172px;font-size:9.5px;line-height:15.5px;text-align:right}
.qmark{position:absolute;left:55px;top:122px;font-size:44px;font-weight:800;color:rgba(255,255,255,.28);line-height:1}
.bar{position:absolute;left:274px;width:450px}
.bar .name{font-size:7px;font-weight:700;height:12px}
.track{height:14px;background:rgba(5,20,60,.45)}
.bar-fill{height:14px;background:linear-gradient(90deg,var(--blue),var(--cyan));font-size:6.5px;font-weight:700;text-align:right;padding-right:6px;line-height:14px}

/* map */
.mapband{position:absolute;left:0;top:972px;width:780px;height:300px;background:linear-gradient(120deg,#e4eaf1 0%,#c6dcf6 35%,#e9edf2 55%,#b4d4f7 70%,#e4e9ef 100%)}
.maptoggle{position:absolute;left:0;top:8px;font-size:6.5px;background:var(--white);padding:3px 5px;color:#333}
.pin{position:absolute;left:383px;top:108px}
.info{position:absolute;left:517px;top:23px;width:218px;height:260px;background:rgba(255,255,255,.94);text-align:center;color:var(--ink)}
.info h5{font-size:9px;font-weight:700;margin-top:6px}
.info p{font-size:7.5px;line-height:15px;color:#444;margin-top:4px}

/* footer */
.footer{position:absolute;left:0;top:1272px;width:780px;height:228px;background:var(--footer);color:var(--white)}
.col{position:absolute;top:34px;width:160px}
.col h6{font-size:11px;font-weight:700;color:var(--cyan)}
.col h6::after{content:"";display:block;width:30px;height:2px;background:var(--white);margin-top:6px}
.news{display:flex;gap:6px;margin-top:14px}
.news:first-of-type{margin-top:12px}
.thumb{width:40px;height:40px;flex:none;background:linear-gradient(150deg,#2d3f66,#c07a3a)}
.news b{display:block;font-size:7.5px;font-weight:700;line-height:9.5px}
.news small{display:block;font-size:6.5px;margin-top:6px;color:#d3e2f7}
.tweet{font-size:7.5px;line-height:14.5px;color:#e2ecfa;margin-top:12px;width:160px}
.tweet .by{font-size:5.5px;color:#b5cbea}
.tweet .by::before{content:"";display:inline-block;width:7px;height:6px;background:var(--cyan);border-radius:3px;margin-right:4px}
.quick-links{display:grid;grid-template-columns:76px 82px;row-gap:6px;font-size:7.5px;color:#e2ecfa;margin-top:13px}
</style>
</head>
<body>
<div class="page">

  <header class="hero">
    <div class="fill-area" role="img" aria-label="Cargo airliner climbing through a bright blue sky"></div>
    <div class="topbar">
      <div class="topbar-links"><span>Newsletter</span><span>Careers</span></div>
      <div class="social" aria-label="Social links"><i></i><i></i><i></i><i></i><i></i></div>
      <div class="fare">GET A FARE RATE</div>
    </div>
    <div class="brand">Northbeam Freight</div>
    <nav class="nav"><span>HOME</span><span>PAGES</span><span>SERVICES</span><span>FLEET</span><span>NEWS</span><span>CALCULATORS</span></nav>
    <div class="welcome">Welcome to</div>
    <h1 class="title">CARGO TRANSPORT</h1>
    <div class="rule"></div>
    <p class="lead">Global turnkey logistics and transportation services via sea, land and air. We will protect you from risk and liability.</p>
    <div class="btn primary">GET A FULL QUOTE</div>
    <div class="btn ghost">FIND OUT MORE</div>

    <form class="quote">
      <h3>GET A QUICK QUOTE</h3>
      <div class="note">* for detailed quote use extended version</div>
      <div class="field" style="top:67px">TRUCKLOAD</div>
      <div class="select" style="top:60px">Select...</div>
      <div class="field" style="top:102px">COMMODITY</div>
      <div class="select" style="top:95px">Select...</div>
      <div class="field" style="top:136px">DIST (MILES)</div>
      <div class="slider"></div>
      <div class="knob">0</div>
      <div class="field" style="top:168px">REFRIGERATED</div>
      <div class="toggle"></div>
      <div class="total"><span class="lbl">TOTAL</span><span class="val">$ 0.00</span></div>
    </form>
    <svg class="next" width="16" height="30" viewBox="0 0 16 30"><path d="M2 2 L14 15 L2 28" fill="none" stroke="#fff" stroke-width="1.2"/></svg>
  </header>

  <section class="services">
    <div class="map-dots" role="img" aria-label="Faint dotted world map"></div>
    <div class="kicker">WHAT WE SHIP</div>
    <h2 class="sec-title">WHAT WE CAN DO<br>FOR YOU</h2>
    <p class="path">http://northbeamfreight.example/assets<br>/fleet/truck_green.png</p>

    <article class="card" style="left:274px;top:44px">
      <svg width="20" height="16" viewBox="0 0 20 16"><rect x="3" y="1" width="14" height="10" rx="1" fill="#1f7bff"/><rect x="5" y="3" width="10" height="6" fill="#fff"/><path d="M0 12h20l-2 3H2z" fill="#1f7bff"/></svg>
      <h4>ELECTRONICS</h4>
      <p>Laptops, phones and home devices packed in padded, sealed cases and tracked door to door across the US and Canada.</p>
    </article>
    <article class="card" style="left:505px;top:44px">
      <svg width="20" height="18" viewBox="0 0 20 18"><path d="M6 1 L1 5 L4 8 L5 7 V17 H15 V7 L16 8 L19 5 L14 1 C13 3 7 3 6 1z" fill="#1f7bff"/></svg>
      <h4>CLOTHING</h4>
      <p>Apparel, footwear and textiles shipped in bulk or single parcels, folded flat or on hangers, kept dry on every route.</p>
    </article>
    <article class="card" style="left:274px;top:171px">
      <svg width="16" height="20" viewBox="0 0 16 20"><path d="M1 1 H11 L15 5 V19 H1z" fill="#1f7bff"/><path d="M4 8h8M4 11h8M4 14h6" stroke="#fff" stroke-width="1.4"/></svg>
      <h4>DOCUMENTS</h4>
      <p>Contracts, letters and legal papers sent by express courier with signed delivery and same day pickup in most cities.</p>
    </article>
    <article class="card" style="left:505px;top:171px">
      <svg width="20" height="18" viewBox="0 0 20 18"><path d="M1 5 L10 1 L19 5 V16 L10 17 L1 16z" fill="#1f7bff"/><path d="M1 5 L10 8 L19 5 M10 8 V17" stroke="#fff" stroke-width="1.2" fill="none"/></svg>
      <h4>OTHER GOODS</h4>
      <p>Anything else you need moved: furniture, parts, gifts and more, quoted fast and handled with the same care.</p>
    </article>
  </section>

  <section class="numbers">
    <div class="fill-area" role="img" aria-label="Highway at dusk with motion-blurred traffic"></div>
    <div class="kicker2">WE ARE THE BEST</div>
    <h2>CARGO IN NUMBERS</h2>
    <div class="qmark">“</div>
    <blockquote>Duis aute irure dolor in reprehenderit in voluptate velit esse cillum dolore eu fugiat nulla pariatur. Excepteur sint occaecat cupidatat non proident.</blockquote>
    <div class="bar" style="top:60px"><div class="name">MARKET SHARE IN CE REGION</div><div class="track"><div class="bar-fill" style="width:75%">75%</div></div></div>
    <div class="bar" style="top:95px"><div class="name">REVENUE GROWTH PER YEAR</div><div class="track"><div class="bar-fill" style="width:61%">61%</div></div></div>
    <div class="bar" style="top:129px"><div class="name">PROFIT GROWTH PER YEAR</div><div class="track"><div class="bar-fill" style="width:54%">54%</div></div></div>
    <div class="bar" style="top:164px"><div class="name">INCREASE IN NUMBER OF LOGISTICS CENTERS</div><div class="track"><div class="bar-fill" style="width:100%">100%</div></div></div>
  </section>

  <section class="mapband" role="img" aria-label="Street map of the harbor district around the main office">
    <div class="maptoggle">Map &nbsp; Satellite</div>
    <svg class="pin" width="26" height="38" viewBox="0 0 26 38"><path d="M13 1 C6 1 1 6 1 13 C1 22 13 37 13 37 C13 37 25 22 25 13 C25 6 20 1 13 1z" fill="#1f7bff"/><circle cx="13" cy="13" r="6" fill="#fff"/><circle cx="13" cy="13" r="3.5" fill="#1f7bff"/></svg>
    <div class="info">
      <svg style="margin-top:30px" width="20" height="22" viewBox="0 0 20 22"><circle cx="10" cy="12" r="8" fill="none" stroke="#333" stroke-width="2"/><path d="M10 12V7M7 2h6" stroke="#333" stroke-width="2"/></svg>
      <h5>WORKING HOURS</h5>
      <p>Mon-Sat 7AM-5PM<br>Sat 9AM-3PM</p>
      <svg style="margin-top:20px" width="20" height="20" viewBox="0 0 20 20"><circle cx="9" cy="11" r="7.5" fill="none" stroke="#333" stroke-width="1.6"/><path d="M1.5 11h15M9 3.5v15M4 6c3 2 7 2 10 0M4 16c3-2 7-2 10 0" fill="none" stroke="#333" stroke-width="1"/></svg>
      <h5>OUR LOCATION</h5>
      <p>418 Harbor Ave NW<br>Bayport</p>
    </div>
  </section>

  <footer class="footer">
    <div class="col" style="left:44px">
      <h6>NEWS</h6>
      <div class="news"><div class="thumb" role="img" aria-label="Cargo plane on a lit runway"></div><div><b>Liberalisation of air cargo industry</b><small>October 9, 2015</small></div></div>
      <div class="news"><div class="thumb" role="img" aria-label="New trucks in the depot"></div><div><b>New trucks arriving</b><small>September 17, 2015</small></div></div>
      <div class="news"><div class="thumb" role="img" aria-label="Warehouse exterior"></div><div><b>New warehouse now operational</b><small>September 16, 2015</small></div></div>
    </div>
    <div class="col" style="left:219px">
      <h6>UPDATES</h6>
      <p class="tweet"><span class="by">@northbeam - 10 hours</span><br>RT @freightweek: @harborlines (@shipsmart) @roadledger &amp; Dana Morrow at #Freight2016 kickoff party @northbeam<br>nbf.example/k2x8</p>
      <p class="tweet"><span class="by">@northbeam - 10 hours</span><br>Live: Freight Week 2016 kick off at Northbeam nbf.example/p4r7</p>
    </div>
    <div class="col" style="left:395px"><h6>PHOTO GALLERY</h6></div>
    <div class="col" style="left:571px">
      <h6>QUICK LINKS</h6>
      <div class="quick-links">
        <span>Electronics</span><span>Clothing</span>
        <span>Documents</span><span>Other goods</span>
        <span>Cost Calculators</span><span>Trucking calculator</span>
        <span>Courier calculator</span><span>Ocean cargo calc</span>
        <span>Air cargo calculator</span><span>Pricing</span>
        <span>FAQs</span>
      </div>
    </div>
  </footer>

</div>
</body>
</html>
```